Company Marketing Flyers for SEO company

Harbourline Search Academy requires a four page A4 color brochure for small businesses who are being marketed to for SEO services.

The brochure is provided to the potential client during a first meeting. So we are looking for nice glossy pictures combined with sufficient text to enable the applicant to make an informed decision.

I have attached a word document that contains the text that may help plus lots of pictures that are on the website that could be used also.

Target Market(s)

small businesses seeking SEO support and assistance

Industry/Entity Type

Marketing

Font styles to use
Sans Serif

Colors
9bcb3c
0555a3
acd036
cadf82
eaf2ce
ffffff

Requirements
Must have
• color photos, glossy, exciting and fun
Nice to have
• happy, quality
Should not have
• scary stuff

```html
<!DOCTYPE html>
<html lang="en">
<head>
<meta charset="utf-8">
<title>Harbourline Search Academy – Brochure</title>
<link href="https://fonts.googleapis.com/css2?family=Open+Sans:wght@300;400;600&display=swap" rel="stylesheet">
<style>
:root{
  --green:#8cbf3f;
  --green-dark:#6f9e2a;
  --lime:#acd036;
  --olive:#9bab3a;
  --pale:#cadf82;
  --mist:#eaf2ce;
  --ink:#2b2b2b;
  --paper:#ffffff;
  --stage:#e9e9e7;
}
*{box-sizing:border-box;margin:0;padding:0}
html,body{width:1200px;height:2260px;overflow:hidden;background:var(--stage)}
body{position:relative;font-family:"Open Sans",Arial,sans-serif;color:var(--ink)}
.page{position:absolute;background:var(--paper);overflow:hidden;box-shadow:0 2px 8px rgba(0,0,0,.18)}
.cover{left:326px;top:45px;width:489px;height:690px}
.spread{left:116px;top:777px;width:972px;height:686px;display:flex;background:none;box-shadow:none;overflow:visible}
.spread .leaf{position:relative;width:486px;height:686px;background:var(--paper);overflow:hidden;box-shadow:0 2px 8px rgba(0,0,0,.18)}
.back{left:326px;top:1508px;width:489px;height:694px}
.photo{position:absolute;left:0;top:0;width:100%}
.cover .photo{height:405px;background:linear-gradient(135deg,#1f3550 0%,#4d6f8f 45%,#c9d4dc 75%,#6d7f8e 100%)}
.back .photo{height:322px;background:linear-gradient(160deg,#d9d2c4 0%,#8d7a63 35%,#3a3f47 60%,#b7b2aa 100%)}
.callout{position:absolute;left:27px;top:22px;color:#fff;font-weight:300}
.callout .label{font-size:16px}
.callout .num{font-size:25px;letter-spacing:.5px}
.facets{position:absolute;right:0;width:100px}
.headline{position:absolute;left:27px;top:372px;width:360px;color:var(--green);font-weight:300;font-size:41px;line-height:1;text-transform:uppercase}
.subhead{position:absolute;left:27px;top:460px;width:370px;font-size:17px;line-height:1.2;color:#111}
.cover .copy{position:absolute;left:27px;top:512px;width:360px}
p,li{font-size:7px;line-height:1.45}
p+p{margin-top:6px}
.brand{position:absolute;color:var(--green);font-weight:300;font-size:17px;white-space:nowrap;display:flex;align-items:center;gap:6px}
.brand::before{content:"";width:9px;height:9px;background:var(--green);border-radius:50%}
.col{position:absolute;top:26px}
h2{color:var(--green);font-weight:300;font-size:14px;line-height:1.05;text-transform:uppercase;margin:10px 0 4px}
.col h2:first-child{margin-top:0}
ul{list-style:none;margin:3px 0 5px}
li{position:relative;padding-left:10px;margin-bottom:2px}
li::before{content:"";position:absolute;left:1px;top:3px;width:4px;height:4px;border-radius:50%;background:var(--green)}
.icons{position:absolute}
.back .info{position:absolute;left:48px;top:365px;width:380px}
.back h2{font-size:15px}
.addr{display:flex;gap:40px;margin:10px 0 14px}
.addr p{color:var(--green);font-weight:600;margin:0}
.contact p{font-size:10px;margin:0}
.contact b{color:var(--green);font-weight:600}
.call{color:var(--green);font-weight:300;font-size:27px;margin-top:14px}
.legal{position:absolute;left:0;right:0;bottom:6px;text-align:center;font-size:5px;color:#333}
</style>
</head>
<body>

<section class="page cover">
  <div class="photo" role="img" aria-label="Photo of a hand tapping a tablet showing an inbound marketing strategy diagram"></div>
  <div class="callout"><div class="label">Call us now</div><div class="num">1300 42 42 77</div></div>
  <svg class="facets" style="top:338px;height:352px" viewBox="0 0 100 352" preserveAspectRatio="none" aria-hidden="true">
    <polygon points="100,0 40,20 100,352" fill="var(--pale)"/>
    <polygon points="100,0 55,120 100,352" fill="var(--lime)"/>
    <polygon points="100,60 20,352 100,352" fill="var(--green)"/>
    <polygon points="100,150 60,352 100,352" fill="var(--green-dark)"/>
  </svg>
  <h1 class="headline">Marketing has changed!</h1>
  <div class="subhead">Rank high on search engines to maintain and grow your business</div>
  <div class="copy">
    <p>Harbourline Search Academy work with organisations to design, implement and oversee an online marketing Search Engine Optimisation (SEO), Social Media optimisation (SMO) and Search Engine Marketing (SEM) strategy. Integral to the strategy is getting your website ranking high on Seekly, Findr and Lookout to increase site visitors and then boost conversions into leads and sales.</p>
    <p>We aim to give your business the tools to hit your competition hard and take from them market share across each product and service.</p>
  </div>
  <div class="brand" style="right:60px;bottom:20px">Harbourline Search Academy</div>
</section>

<section class="page spread">
  <div class="leaf">
    <div class="col" style="left:46px;width:200px">
      <h2>Online Marketing</h2>
      <p>Online marketing is often referred to as digital marketing, internet or web marketing. Online marketing activities include, but are not limited to:</p>
      <ul><li>Search Engine Optimisation (SEO)</li><li>Search Engine Marketing (SEM)</li><li>Social Media Marketing</li><li>Direct marketing</li><li>Display advertising</li><li>Email direct marketing</li><li>Social Media Optimisation (SMO).</li></ul>
      <p>The fundamental concept with online marketing is the focus on the customer and building comprehensive solutions to meet their search needs.</p>
      <p>Harbourline Search Academy incorporate each of these activities into the development of a robust and nimble online marketing – business growth strategy to enable you to compete within an aggressive and competitive environment so you can break into, grow and then maintain SEO and SMO rankings for each of your products and services.</p>
      <p>Harbourline online marketing staff work on each of these activities and implement, tinker, arrange and then re-arrange a myriad of SEO, SMO and SEM below listed techniques to broadcast your organisations products and services within your region of business.</p>
      <h2>Search Engine Optimisation (SEO)</h2>
      <p>We create great and unique content on your website pages that focus upon what your customer needs to know and wants to find:</p>
      <ul><li>SEO friendly URL's;</li><li>Integrate key words as identified from a key-word planner (Seekly Planner);</li><li>Anchor text, Meta Tags, Meta Description;</li><li>Blogs for business;</li><li>Question and answer;</li><li>Live chat;</li><li>Cross linking;</li><li>URL normalisation;</li><li>Copywriting;</li><li>301 redirects;</li><li>Multiple URL's;</li><li>Multiple ISP's.</li></ul>
    </div>
    <div class="col" style="left:257px;width:210px">
      <h2>Social Media Optimisation (SMO)</h2>
      <p>We create and coach you how to maintain exciting and useful social media:</p>
      <ul><li>Friendbook for business site;</li><li>Snapgram for business site;</li><li>ProLink site;</li><li>Chirper for business account;</li><li>E-Marketing newsletters.</li></ul>
      <h2>Broadcast Marketing</h2>
      <p>Building a successful marketing strategy should also incorporate technologies that are not solely online strategies. The addition of database marketing to support an online marketing strategy can time efficiently and cost effectively grow business leads and support existing clients, via:</p>
      <ul><li>Mail</li><li>SMS Broadcasts</li><li>Email marketing</li><li>Bulk Facsimile Broadcasts</li></ul>
      <p>Harbourline advisors will assess your organisations existing databases and suggest how the creation or variance to existing practices can help generate new and repeat business for your organisation.</p>
    </div>
    <svg class="icons" style="left:230px;top:360px" width="256" height="326" viewBox="0 0 256 326" aria-hidden="true">
      <g transform="translate(31 4)">
        <circle cx="48" cy="40" r="33" fill="var(--green)"/>
        <path d="M34 48h28a8 8 0 0 0-2-16 11 11 0 0 0-21-2 8 8 0 0 0-5 18z" fill="#fff"/>
        <path d="M48 56V40m-6 6 6-6 6 6" stroke="var(--green)" stroke-width="3" fill="none"/>
      </g>
      <g transform="translate(50 57)">
        <circle cx="124" cy="46" r="32" fill="var(--olive)"/>
        <path d="M110 60l28-28M110 32l28 28" stroke="#fff" stroke-width="5" stroke-linecap="round"/>
      </g>
      <g transform="translate(41 60)">
        <circle cx="85" cy="110" r="40" fill="var(--green)"/>
        <rect x="64" y="94" width="42" height="28" rx="4" fill="#fff"/>
        <path d="M72 122l-4 10 12-10z" fill="#fff"/>
        <path d="M71 103h28M71 109h28M71 115h20" stroke="var(--green)" stroke-width="3"/>
      </g>
      <g transform="translate(39 273) scale(1.4) translate(-82 -200)">
        <circle cx="82" cy="200" r="48" fill="var(--olive)"/>
        <circle cx="76" cy="192" r="18" fill="none" stroke="#fff" stroke-width="7"/>
        <path d="M89 206l20 20" stroke="#fff" stroke-width="10" stroke-linecap="round"/>
      </g>
    </svg>
  </div>
  <div class="leaf">
    <div class="col" style="left:27px;width:200px">
      <h2>Small Business Pack</h2>
      <p>Harbourline Search Academy will implement an online marketing growth strategy that seeks to get your website ranking high on search engines allowing you to take from the competition market share for each product and service your small business offers. Products and services you receive include:</p>
      <ul><li>Branding (stationery, newsletter templates);</li><li>Domain name registration and hosting (3 URL annually);</li><li>Website design and creation/recreate (1 website and 2 sub website annually);</li><li>Search Engine Optimisation (SEO techniques applied weekly to each site);</li><li>Social Media sites (Friendbook, Chirper, ProLink, Snapgram);</li><li>Social Media Optimisation (SMO techniques applied weekly to each site);</li><li>Online advertising (Newsletter templates, banners, photos, Pay Per Click (budget limited);</li><li>Broadcast marketing monthly (Fax, Mail, SMS);</li><li>Conversion Rate Optimisation (Copywriting, site analysis reports);</li><li>Coaching and overseeing blogs, question and answer, social media, key word and identifying industry updates.</li></ul>
      <h2>Fixed Monthly Fee</h2>
      <p>The standard fee charged for the aforementioned services is $1,800.00 per month plus GST. We require that you commit to a 12 month campaign but our recommendation is that you commit to at least a 24 month campaign to achieve the best long term sustained results.</p>
      <p>We understand this is a serious investment but we are about producing serious results and if your business is ready to grow then our proven techniques will see that you will grow.</p>
      <h2>What You Receive</h2>
      <ul><li>An online marketing – business growth strategy plan</li><li>A logo, stationery, websites, social media sites, advertising template, banner template, databases, blog, marketing techniques, broadcast gateways and associated intellectual property (IP);</li><li>A monthly site report that includes ranking statistics and conversion analysis with the view to ongoing improvement of increasing sales or leads as per the online marketing strategy.</li></ul>
    </div>
    <div class="col" style="left:237px;width:195px">
      <h2>What's expected from you and your staff?</h2>
      <p>We will require that you or another designated person/s within your organisation:</p>
      <ul><li>To be trained in and then maintain online enquiries, blogs, social media uploads, web page unique content creation and content for Fax, Email, SMS and Newsletter Broadcasts;</li><li>Liaise with our Harbourline studio technicians regarding your business products, services and industry updates;</li><li>An openness from the small business to allow the website to integrate and become part of your business practice;</li><li>Learn to plan for and think about business operations in terms of the online marketing strategy to enable the business to continue to achieve long term sustained SEO and SMO results.</li></ul>
      <h2>Will this work for my business?</h2>
      <p>In short, yes. But you need to be able to afford it, commit to the journey AND be ready to handle the sales activity that comes your way. An E-commerce (online sales) website needs to handle increases in orders. Lead generation websites need to be able to process an increase in the number of new leads. But, growth in business does come with challenges and if you have read this far then you are ready to take the next step.</p>
    </div>
    <svg class="facets" style="top:0;height:686px;width:70px" viewBox="0 0 70 686" preserveAspectRatio="none" aria-hidden="true">
      <polygon points="70,0 20,0 70,686" fill="var(--pale)"/>
      <polygon points="70,0 45,0 40,686 70,686" fill="var(--lime)"/>
      <polygon points="70,200 10,686 70,686" fill="var(--green)"/>
      <polygon points="70,380 45,686 70,686" fill="var(--green-dark)"/>
    </svg>
    <svg class="icons" style="left:265px;top:465px" width="150" height="130" viewBox="0 0 150 130" aria-hidden="true">
      <circle cx="118" cy="28" r="22" fill="var(--olive)"/>
      <rect x="106" y="18" width="24" height="17" rx="3" fill="#fff"/>
      <path d="M111 35l-2 6 8-6z" fill="#fff"/>
      <path d="M110 24h16M110 29h12" stroke="var(--olive)" stroke-width="2"/>
      <circle cx="60" cy="72" r="50" fill="var(--green)"/>
      <path d="M40 92h6v-12h-6zM52 92h6v-18h-6zM64 92h6v-26h-6zM76 92h6v-34h-6z" fill="#fff"/>
      <path d="M38 74l44-32m-8 0h8v8" stroke="#fff" stroke-width="3" fill="none"/>
    </svg>
    <div class="brand" style="right:85px;bottom:26px">Harbourline Search Academy</div>
  </div>
</section>

<section class="page back">
  <div class="photo" role="img" aria-label="Photo of a person typing on a laptop showing an ROI growth chart"></div>
  <svg class="facets" style="top:0;height:420px" viewBox="0 0 100 420" preserveAspectRatio="none" aria-hidden="true">
    <polygon points="100,0 20,0 100,420" fill="var(--pale)"/>
    <polygon points="100,0 50,0 70,300 100,420" fill="var(--lime)"/>
    <polygon points="100,0 80,0 100,260" fill="var(--green)"/>
    <polygon points="100,120 75,260 100,420" fill="var(--green-dark)"/>
  </svg>
  <div class="info">
    <h2>For More Information</h2>
    <p>Harbourline Search Academy was established on 18 November 2015 to assist business around Australia integrate proven internet marketing techniques and help them grow inbound enquiries, online sales and provide greater solutions to existing and future clients.</p>
    <p>Harbourline Search has an intimate understanding of Search Engine Optimisation (SEO), Pay per Click (PPC), Social Media Optimisation (SMO), online advertising and building business brands across Australia that compete with large organisations and take from them market share.</p>
    <div class="addr">
      <p>Harbourline Search Academy<br>Level 9, 212 Wattle Street<br>Melbourne VIC 3000</p>
      <p>Level 4, 18 Ferry Lane<br>Sydney NSW 2000</p>
    </div>
    <div class="contact">
      <p><b>EMAIL:</b> hello@harbourlinesearch.com.au</p>
      <p><b>WEB:</b> www.harbourlinesearch.com.au</p>
    </div>
    <div class="call">CALL 1300 42 42 77</div>
  </div>
  <div class="brand" style="right:60px;bottom:30px">Harbourline Search Academy</div>
  <div class="legal">Harbourline Search Pty Ltd ACN 612 448 190 trading as Harbourline Search Academy</div>
</section>

</body>
</html>
```